Adventurous female pilot

I am looking for a personal business card, for a very well qualified female pilot, with a lot of aviation experience.

Currently an airline pilot, have worked as a bush pilot in Africa, looking to get into corporate aviation, or private jet owners.
Want a classy looking card for networking...

Could be interested in a retro\vintage look also?!

An idea,, is an african sunset background, with my wings\logo on it
Updates

I just want to say thank you to all of your for your amazing designs!

I have been very busy flying this past week , so not had a chance to be on the computer much.
But I provide some feedback, and conclusions very soon!
Thank you again.

Marla

Reason: Still waiting on a couple of revisions to be 100% about my choice!

Target Market(s)

corporate aviation, private jet owners, casino's,
General audience.
networking

Industry/Entity Type

Airline

Requirements
Nice to have
• Classy, edgy, sexy, but also feminine

```html
<!DOCTYPE html>
<html lang="en">
<head>
<meta charset="utf-8">
<title>Marla Hollis – Business Card</title>
<link rel="stylesheet" href="https://fonts.googleapis.com/css2?family=Cinzel:wght@500&family=Arimo:wght@400&display=swap">
<style>
  :root {
    --page-bg: #ffffff;
    --card-light: #f4f4f4;
    --band-pink: #dc5ea3;
    --band-magenta: #a00d5d;
    --card-dark: #1d1d1f;
    --card-dark-soft: #2a2a2d;
    --name-colour: #9a0f5e;
    --contact-colour: #ffffff;
  }
  html, body {
    margin: 0;
    padding: 0;
    width: 1200px;
    height: 1000px;
    overflow: hidden;
    background: var(--page-bg);
  }
  .canvas {
    position: relative;
    width: 1200px;
    height: 1000px;
  }
  .business-card {
    position: absolute;
    left: 75px;
    top: 200px;
    width: 1050px;
    height: 600px;
    border-radius: 40px;
    overflow: hidden;
    box-shadow: 0 2px 6px rgba(0,0,0,0.25);
  }
  .card-shapes {
    position: absolute;
    inset: 0;
    display: block;
  }
  .plane-emblem {
    position: absolute;
    left: 33px;
    top: 90px;
    width: 170px;
    height: 100px;
    border-radius: 50px 10px 50px 10px;
    background: linear-gradient(135deg, #d9d9d9, #8a8a8a);
  }
  .holder-name {
    position: absolute;
    left: 220px;
    top: 128px;
    margin: 0;
    font-family: "Cinzel", "Trajan Pro", serif;
    font-weight: 500;
    font-size: 62px;
    line-height: 1;
    letter-spacing: 6px;
    color: var(--name-colour);
    white-space: nowrap;
  }
  .contact-list {
    position: absolute;
    left: 501px;
    top: 438px;
    margin: 0;
    padding: 0;
    list-style: none;
    font-family: "Arimo", Arial, sans-serif;
    font-size: 24px;
    line-height: 32px;
    letter-spacing: 1.3px;
    color: var(--contact-colour);
    white-space: nowrap;
  }
</style>
</head>
<body>
<main class="canvas">
  <article class="business-card">
    <svg class="card-shapes" width="1050" height="600" viewBox="0 0 1050 600" aria-hidden="true">
      <defs>
        <linearGradient id="dark-fill" x1="0" y1="0" x2="0" y2="1">
          <stop offset="0" stop-color="var(--card-dark-soft)"/>
          <stop offset="1" stop-color="var(--card-dark)"/>
        </linearGradient>
      </defs>
      <rect class="light-field" width="1050" height="600" fill="var(--card-light)"/>
      <path class="pink-band" d="M0,398 C420,392 790,205 975,0 L1050,0 L1050,600 L0,600 Z" fill="var(--band-pink)"/>
      <path class="magenta-band" d="M0,428 C450,418 830,225 1010,0 L1050,0 L1050,600 L0,600 Z" fill="var(--band-magenta)"/>
      <path class="dark-field" d="M0,431 C470,426 880,255 1050,42 L1050,600 L0,600 Z" fill="url(#dark-fill)"/>
    </svg>
    <div class="plane-emblem" role="img" aria-label="Line illustration of a jet aircraft taking off"></div>
    <h1 class="holder-name">Marla Hollis</h1>
    <ul class="contact-list">
      <li>Email: marlachollis@skyroutemail.com</li>
      <li>Cell US: +1 555-214-3096</li>
      <li>Cell Taipei: +886 912-408-273</li>
    </ul>
  </article>
</main>
</body>
</html>
```